Global social media analytics company needs business card design

We need an updated business card design to align with our new website - brightquillo.net -

I would also like a favicon designed as well.

Target Market(s)

CEOs, CMOs go big companies

Industry/Entity Type

Business

Contact Information for Business Card

Room for the following:
Address
Main telephone
Direct telephone or cell phone
twitter handle

Colors
aaaaaa

Requirements
Must have
• Attention to detail; style.
• Use the logo color from our website - which is gray

```html
<!DOCTYPE html>
<html lang="en">
<head>
<meta charset="utf-8">
<title>brightquillo stationery</title>
<link href="https://fonts.googleapis.com/css2?family=Exo+2:wght@600&family=Questrial&family=Open+Sans:wght@700&display=swap" rel="stylesheet">
<style>
  :root {
    --charcoal: #414342;
    --paper: #ffffff;
    --backdrop: #d6d6d6;
    --light-text: #e6e6e6;
    --mark-faint: #cfcfcf;
    --watermark: #4b4d4c;
  }
  * { margin: 0; padding: 0; box-sizing: border-box; }
  html, body { width: 1200px; height: 1000px; overflow: hidden; }
  body { background: var(--backdrop); position: relative; font-family: "Questrial", sans-serif; }

  .sheet { position: absolute; background: var(--paper); overflow: hidden; }

  /* Letterhead */
  .letterhead { left: 180px; top: 66px; width: 616px; height: 870px; }
  .letterhead__band { position: absolute; left: 0; top: 0; width: 100%; height: 73px; background: var(--charcoal); }
  .brand { position: absolute; display: flex; align-items: center; font-family: "Exo 2", sans-serif; font-weight: 600; white-space: nowrap; }
  .brand__dot { border-radius: 50%; flex: none; }

  .header-mark { position: absolute; left: 0; top: 0; width: 100%; height: 73px; }
  .header-mark__dot { position: absolute; left: -2px; top: 20px; width: 66px; height: 66px; border-radius: 50%; background: var(--paper); }
  .header-mark__name { position: absolute; left: 82px; top: 38px; font-family: "Exo 2", sans-serif; font-weight: 600; font-size: 30px; line-height: 1; color: var(--paper); white-space: nowrap; }

  .contact { position: absolute; list-style: none; color: var(--light-text); font-size: 7px; line-height: 10.5px; }
  .contact li { display: flex; align-items: center; gap: 5px; }
  .contact svg { width: 7px; height: 7px; fill: var(--light-text); flex: none; }
  .letterhead .contact { left: 490px; top: 16px; }
  .brand--footer { left: 490px; top: 828px; color: var(--mark-faint); font-size: 12px; }
  .brand--footer .brand__dot { width: 26px; height: 26px; background: var(--mark-faint); margin-right: 5px; }

  /* Business card front */
  .card-front { left: 838px; top: 194px; width: 269px; height: 157px; background: var(--charcoal); }
  .card-front .brand--card { left: 13px; top: 40px; color: var(--paper); font-size: 13px; }
  .card-front .brand--card .brand__dot { width: 26px; height: 26px; background: var(--paper); margin-right: 5px; }
  .card-front__name { position: absolute; left: 19px; top: 84px; font-family: "Open Sans", sans-serif; font-weight: 700; font-size: 7.5px; color: var(--paper); }
  .card-front .contact { left: 19px; top: 101px; }
  .brand--watermark { left: 0; top: 122px; color: var(--watermark); font-size: 27px; }
  .brand--watermark .brand__dot { width: 36px; height: 36px; background: var(--watermark); margin-right: 40px; }

  /* Business card back */
  .card-back { left: 838px; top: 368px; width: 269px; height: 157px; }
  .card-back .brand--center { left: 53px; top: 57px; color: var(--charcoal); font-size: 18px; }
  .card-back .brand--center .brand__dot { width: 42px; height: 42px; background: var(--charcoal); margin-right: 6px; }
</style>
</head>
<body>
<svg width="0" height="0" style="position:absolute" aria-hidden="true">
  <symbol id="icon-phone" viewBox="0 0 10 10"><path d="M1 4c0-2 2-3 4-3s4 1 4 3v1H7V4H3v1H1zM3 5h4l1 3H2z"/></symbol>
  <symbol id="icon-mail" viewBox="0 0 10 10"><path d="M0 2h10v6H0zM1 3v.5L5 6l4-2.5V3L5 5.5z"/></symbol>
  <symbol id="icon-pin" viewBox="0 0 10 10"><path d="M5 0a3.5 3.5 0 0 1 3.5 3.5C8.5 6 5 10 5 10S1.5 6 1.5 3.5A3.5 3.5 0 0 1 5 0zm0 2a1.5 1.5 0 1 0 0 3 1.5 1.5 0 0 0 0-3z"/></symbol>
</svg>

<section class="sheet letterhead">
  <div class="letterhead__band"></div>
  <div class="header-mark">
    <span class="header-mark__dot"></span>
    <span class="header-mark__name">brightquillo</span>
  </div>
  <ul class="contact">
    <li><svg><use href="#icon-phone"/></svg>000 0000</li>
    <li><svg><use href="#icon-phone"/></svg>000 0000</li>
    <li><svg><use href="#icon-mail"/></svg>email@quillmail.net</li>
    <li><svg><use href="#icon-pin"/></svg>PO Box 0000 Harbourview WA 6000</li>
  </ul>
  <div class="brand brand--footer"><span class="brand__dot"></span>brightquillo</div>
</section>

<section class="sheet card-front">
  <div class="brand brand--watermark"><span class="brand__dot"></span>brightquillo</div>
  <div class="brand brand--card"><span class="brand__dot"></span>brightquillo</div>
  <p class="card-front__name">Name Surname</p>
  <ul class="contact">
    <li><svg><use href="#icon-phone"/></svg>000 0000</li>
    <li><svg><use href="#icon-mail"/></svg>email@quillmail.net</li>
    <li><svg><use href="#icon-pin"/></svg>PO Box 0000 Harbourview WA 6000</li>
  </ul>
</section>

<section class="sheet card-back">
  <div class="brand brand--center"><span class="brand__dot"></span>brightquillo</div>
</section>
</body>
</html>
```